Flyer YOga studio

I need a double sided DL flyer (landscape) with my yoga studio details on one side and my timetable on the back.
Updates

It looks like a lot of my info didn't save the orignal brief.

here is some information.

On the front side - Logo to be centred on white background.

Underneath text
$20 for 7 days unlimited yoga/pilates/run group
$99 for 1 month unlimited

also to be included - Location: Upstairs, 17 West Parade Linwood 3187
0428 619354
info@hollowmerrick.com.au
www.hollowmerrick.com.au

ON back side - Timetable only

Requirements
Must have
• Following text should be on front side

the logo
New clients offer: $20 for 7 days of Yoga
$99 - 1 month unlimited

Location: Upstairs, 17 West Parade
Linwood VIC 3187
info@hollowmerrick.com.au/0428 619354

The following text:
Stretch...strength...Run
Any order you like...pick all or one. Only fear holds you back from experiencing any of these. We teach all our classes to what is happening in your body in this moment with an eye for alignment, correct muscle recruitment and breath awareness.

On the back:
Class descriptions:
Yoga: Flowing Vinyasa classes that heat the body through dynamic movements and slowing down for deep hip openers and relaxation.
Pilates: Mat classes for healthy bodies using a systematic sequencing of exercises that works the whole body, developing strength, flexibility and mindfulness.
Run groups: A non competitive session where you set the goals and we help you meet them, whether it getting to the corner and back or your first marathon.

```html
<!DOCTYPE html>
<html lang="en">
<head>
<meta charset="utf-8">
<title>Hollow Merrick – DL Flyer</title>
<link rel="stylesheet" href="https://fonts.googleapis.com/css2?family=Open+Sans:wght@400;600;700;800&display=swap">
<style>
  :root {
    --bg: #ececec;
    --paper: #ffffff;
    --ink: #555555;
    --ink-soft: #8a8a8a;
    --grey-band: #d3d3d3;
    --ring: #d9d9d9;
    --yellow: #ffdd00;
    --blue: #1ab1e8;
    --web-blue: #1a93c9;
    --red: #e8202a;
    --orange: #f58a1f;
    --purple: #6a6fbd;
    --green: #3dae3f;
    --teal: #37b6c4;
    --pink: #e8407f;
    --line: #e3e3e3;
    --dash: #c9c9c9;
  }
  * { box-sizing: border-box; margin: 0; padding: 0; }
  html, body { width: 1200px; height: 1000px; overflow: hidden; }
  body {
    background: var(--bg);
    font-family: "Open Sans", Arial, sans-serif;
    color: var(--ink);
    position: relative;
  }

  .card {
    position: absolute;
    left: 40px;
    width: 1120px;
    height: 450px;
    background: var(--paper);
    overflow: hidden;
    border: 1px solid #d6d6d6;
  }
  .card--front { top: 30px; }
  .card--back { top: 520px; }

  .wave { position: absolute; inset: 0; width: 100%; height: 100%; }
  .wave__grey { fill: var(--grey-band); }
  .wave__yellow { fill: var(--yellow); }

  /* ---------- Front ---------- */
  .brand {
    position: absolute;
    left: 60px;
    top: 170px;
    width: 460px;
    display: flex;
    align-items: center;
    justify-content: center;
    gap: 16px;
  }
  .brand__dot {
    width: 38px; height: 38px;
    border-radius: 50%;
    background: var(--orange);
    flex: none;
  }
  .brand__name {
    font-size: 40px;
    font-weight: 700;
    letter-spacing: 2px;
    color: #7d7d7d;
    text-transform: uppercase;
    white-space: nowrap;
  }

  .contact {
    position: absolute;
    left: 42px;
    top: 300px;
    font-size: 15.5px;
    color: var(--ink-soft);
    line-height: 24px;
  }
  .contact__sep { color: var(--blue); margin: 0 6px; }
  .contact__web {
    margin-top: 8px;
    font-weight: 700;
    font-size: 16px;
    color: var(--web-blue);
  }

  .offer {
    position: absolute;
    left: 785px;
    top: 0;
    width: 240px;
    height: 160px;
  }
  .offer svg { position: absolute; inset: 0; width: 240px; height: 160px; }
  .offer__ring { fill: none; stroke: var(--ring); stroke-width: 4; }
  .offer__disc { fill: var(--blue); }
  .offer__text {
    position: absolute;
    left: 0; right: 0; top: 16px;
    text-align: center;
    color: #ffffff;
    font-size: 15px;
    line-height: 1.18;
  }
  .offer__price { font-size: 27px; font-weight: 700; line-height: 1.1; }

  .pitch {
    position: absolute;
    right: 42px;
    top: 292px;
    width: 500px;
    text-align: right;
  }
  .pitch__title {
    font-size: 22px;
    font-weight: 800;
    color: var(--red);
    letter-spacing: 0.3px;
  }
  .pitch__body {
    margin-top: 6px;
    font-size: 15px;
    line-height: 21px;
    color: var(--ink);
  }

  /* ---------- Back ---------- */
  .timetable {
    position: absolute;
    left: 30px;
    top: 14px;
    width: 1060px;
    border-collapse: collapse;
    table-layout: fixed;
    z-index: 0;
  }
  .timetable col.time-col { width: 100px; }
  .timetable th { height: 44px; vertical-align: middle; }
  .day {
    display: inline-block;
    width: 34px; height: 34px;
    border-radius: 50%;
    background: var(--blue);
    color: #ffffff;
    font-size: 14px;
    font-weight: 700;
    line-height: 34px;
    text-align: center;
  }
  .day--wide { font-size: 13px; }
  .timetable td {
    height: 23px;
    border-bottom: 1px solid var(--line);
    text-align: center;
    font-size: 12.5px;
    font-weight: 700;
    white-space: nowrap;
    background: linear-gradient(to right, transparent calc(50% - 0.5px), var(--dash) calc(50% - 0.5px), var(--dash) calc(50% + 0.5px), transparent calc(50% + 0.5px));
    background-size: 100% 4px;
  }
  .timetable td.time {
    text-align: left;
    font-weight: 400;
    font-size: 12px;
    color: var(--ink);
    background: none;
    padding-left: 6px;
  }
  .cls--yoga60 { color: var(--red); }
  .cls--yoga75 { color: var(--orange); }
  .cls--express { color: var(--purple); }
  .cls--express span { font-weight: 400; }
  .cls--pilates { color: var(--green); }
  .cls--run { color: var(--teal); }
  .cls--kids { color: var(--pink); }

  .back-wave { z-index: 1; }

  .legend {
    position: absolute;
    left: 36px;
    top: 294px;
    font-size: 12.5px;
    line-height: 17px;
    color: var(--ink);
    z-index: 2;
  }
  .legend b { font-weight: 700; }

  .desc {
    position: absolute;
    font-size: 12.5px;
    line-height: 16px;
    color: #3f3f3f;
    z-index: 2;
  }
  .desc b { font-weight: 700; }
  .desc--yoga { right: 420px; top: 366px; width: 270px; text-align: right; }
  .desc--side { left: 740px; top: 306px; width: 350px; }
  .desc--side p + p { margin-top: 2px; }
</style>
</head>
<body>

<!-- Front side -->
<section class="card card--front" aria-label="Flyer front">
  <svg class="wave" viewBox="0 0 1120 450" preserveAspectRatio="none" aria-hidden="true">
    <path class="wave__grey" d="M0,392 C250,402 500,372 700,322 C880,277 1000,258 1120,262 L1120,450 L0,450 Z"/>
    <path class="wave__yellow" d="M0,408 C250,418 500,388 700,338 C880,293 1000,274 1120,278 L1120,450 L0,450 Z"/>
  </svg>

  <div class="brand">
    <span class="brand__dot" aria-hidden="true"></span>
    <span class="brand__name">Hollow Merrick</span>
  </div>

  <div class="offer">
    <svg viewBox="0 0 240 160" aria-hidden="true">
      <circle class="offer__ring" cx="120" cy="40" r="118"/>
      <circle class="offer__disc" cx="120" cy="40" r="106"/>
    </svg>
    <div class="offer__text">
      <div>New clients offer</div>
      <div class="offer__price">$20</div>
      <div>(7 days of Yoga)</div>
      <div style="margin-top:6px">1 month unlimited</div>
      <div class="offer__price">$99</div>
    </div>
  </div>

  <address class="contact" style="font-style:normal">
    <div>Upstairs, 17 West Parade<span class="contact__sep">•</span>Linwood, VIC 3187</div>
    <div>0428 619 354<span class="contact__sep">•</span>info@hollowmerrick.com.au</div>
    <div class="contact__web">www.hollowmerrick.com.au</div>
  </address>

  <div class="pitch">
    <h2 class="pitch__title">STRETCH . . . STRENGTH . . . RUN</h2>
    <p class="pitch__body">Any order you like...pick all or one. Only fear holds you back from experiencing any of these. We teach all our classes to what is happening in your body in this moment with an eye for alignment, correct muscle recruitment and breath awareness.</p>
  </div>
</section>

<!-- Back side -->
<section class="card card--back" aria-label="Flyer back – timetable">
  <table class="timetable">
    <colgroup>
      <col class="time-col"><col><col><col><col><col><col><col>
    </colgroup>
    <thead>
      <tr>
        <th></th>
        <th><span class="day">M</span></th>
        <th><span class="day">T</span></th>
        <th><span class="day">W</span></th>
        <th><span class="day day--wide">TH</span></th>
        <th><span class="day">F</span></th>
        <th><span class="day">S</span></th>
        <th><span class="day">S</span></th>
      </tr>
    </thead>
    <tbody>
      <tr><td class="time">6:15 am</td><td></td><td class="cls--yoga60">YOGA</td><td></td><td class="cls--run">RUN GROUP</td><td class="cls--yoga60">YOGA</td><td></td><td></td></tr>
      <tr><td class="time">7:00 am</td><td></td><td></td><td></td><td></td><td></td><td class="cls--run">RUN GROUP</td><td></td></tr>
      <tr><td class="time">9:30 am</td><td class="cls--yoga75">YOGA</td><td class="cls--yoga75">YOGA</td><td class="cls--yoga75">YOGA</td><td class="cls--yoga75">YOGA</td><td class="cls--yoga75">YOGA</td><td class="cls--yoga75">YOGA</td><td class="cls--yoga75">YOGA</td></tr>
      <tr><td class="time">11:00 am</td><td></td><td></td><td></td><td></td><td class="cls--pilates">PILATES</td><td></td><td></td></tr>
      <tr><td class="time">12:15 pm</td><td class="cls--express">EXPRESS <span>Pilates</span></td><td></td><td class="cls--express">EXPRESS <span>Yoga</span></td><td></td><td class="cls--express">EXPRESS <span>Yoga</span></td><td></td><td></td></tr>
      <tr><td class="time">4:00 pm</td><td class="cls--kids">KIDS YOGA</td><td></td><td></td><td></td><td></td><td></td><td></td></tr>
      <tr><td class="time">6:00 pm</td><td></td><td class="cls--pilates">PILATES</td><td></td><td class="cls--yoga60">YOGA</td><td></td><td></td><td></td></tr>
      <tr><td class="time">6:15 pm</td><td class="cls--run">RUN GROUP</td><td></td><td class="cls--run">RUN GROUP</td><td></td><td></td><td></td><td></td></tr>
      <tr><td class="time">7:15 pm</td><td></td><td class="cls--yoga75">YOGA</td><td class="cls--yoga75">YOGA</td><td class="cls--pilates">PILATES</td><td></td><td></td><td></td></tr>
      <tr><td class="time">7:30 pm</td><td class="cls--yoga75">YOGA</td><td></td><td></td><td></td><td></td><td></td><td></td></tr>
    </tbody>
  </table>

  <svg class="wave back-wave" viewBox="0 0 1120 450" preserveAspectRatio="none" aria-hidden="true">
    <path class="wave__grey" d="M0,384 C300,404 560,340 780,298 C940,268 1040,258 1120,262 L1120,450 L0,450 Z"/>
    <path class="wave__yellow" d="M0,398 C300,418 560,354 780,312 C940,282 1040,272 1120,276 L1120,450 L0,450 Z"/>
  </svg>

  <div class="legend">
    <div><b class="cls--yoga60">YOGA:</b> 60 minute classes</div>
    <div><b class="cls--yoga75">YOGA:</b> 75 minute classes</div>
    <div><b class="cls--express">EXPRESS:</b> 45 minutes classes</div>
    <div><b class="cls--pilates">PILATES:</b> 60 minutes classes</div>
  </div>

  <p class="desc desc--yoga"><b class="cls--yoga75">YOGA:</b> Flowing Vinyasa classes that heat the body through dynamic movements and slowing down for deep hip openers and relaxation.</p>

  <div class="desc desc--side">
    <p><b class="cls--pilates">PILATES:</b> Open mat classes for healthy bodies using a systematic sequencing of exercises that works the whole body, developing strength, flexibility and mindfulness.</p>
    <p><b class="cls--run">RUN GROUPS:</b> A non competitive session where you set the goals and we help you meet them, whether it getting to the corner and back or your first marathon.</p>
  </div>
</section>

</body>
</html>
```